Property management company looking for modern card design

We at Blue Maple Holdings provides property management services for its residential and commercial properties, with expertise in all categories of multifamily, industrial and office projects throughout California.

We need a business card design that is professional and modern designed business card. In our field, clients get hundreds of business cards, we would like our card to stand out.

Please avoid small print.

Target Market(s)

Professionals and high end clients

Industry/Entity Type

Financial Planning

Contact Information for Business Card

Company Name: Blue Maple Holdings, Name, email, license #, phone number, website bluemapleholdings.example

Font styles to use
Sans Serif

Requirements
Must have
• The card design needs to be adaptable because there is a possibly we will be expanding into different sectors other than real estate. The card design should be focused on financial planning and asset management.
Nice to have
• Modern and simple business card. Eye catching. Non-standard size/shaped cards would be great.
• bluemapleholdings.example
Should not have
• Too many bright color or any pictures or shapes of real estate stuff.

```html
<!DOCTYPE html>
<html lang="en">
<head>
<meta charset="utf-8">
<title>Blue Maple Holdings – Business Card</title>
<link rel="stylesheet" href="https://fonts.googleapis.com/css2?family=Arimo:wght@400;700&family=PT+Serif:wght@400&display=swap">
<style>
  :root {
    --stage: #2b2b2b;
    --card: #f4f4f4;
    --wine: #7a1018;
    --wine-deep: #5e0b12;
    --red: #c8102e;
    --ink: #2a2a2a;
    --star: #e8b4bc;
    --on-wine: #f1dede;
  }
  * { box-sizing: border-box; margin: 0; padding: 0; }
  html, body { width: 1200px; height: 997px; overflow: hidden; }
  body {
    background: var(--stage);
    font-family: "Arimo", Arial, sans-serif;
    position: relative;
  }
  .card {
    position: absolute;
    width: 560px;
    height: 320px;
    border-radius: 18px;
    background: linear-gradient(180deg, #ffffff 0%, var(--card) 100%);
    overflow: hidden;
    box-shadow: 0 18px 40px rgba(0,0,0,.55);
  }
  .card--front { left: 60px; top: 130px; }
  .card--back { left: 580px; top: 520px; }

  .skyline-band {
    position: absolute;
    left: 0; right: 0; bottom: 0;
    background: linear-gradient(180deg, var(--wine) 0%, var(--wine-deep) 100%);
  }
  .card--front .skyline-band { top: 170px; }
  .card--back .skyline-band { top: 225px; }

  .company-name {
    position: absolute;
    font-family: "Arimo", Arial, sans-serif;
    font-weight: 400;
    color: var(--ink);
    white-space: nowrap;
  }
  .card--front .company-name { left: 0; right: 0; top: 72px; text-align: center; font-size: 26px; }
  .card--back .company-name { right: 30px; top: 40px; font-size: 20px; }

  .star {
    position: absolute;
    left: 48px; top: 68px;
    width: 36px; height: 36px;
  }

  .tagline {
    position: absolute;
    left: 40px; right: 40px; top: 196px;
    font-family: "PT Serif", Georgia, serif;
    font-size: 17px;
    line-height: 1.55;
    color: var(--on-wine);
    text-align: center;
    letter-spacing: .5px;
  }

  .rule {
    position: absolute;
    left: 210px; right: 30px; top: 100px;
    height: 2px;
    background: var(--wine);
  }

  .person { position: absolute; left: 34px; top: 84px; }
  .person__name { font-size: 24px; font-weight: 700; color: var(--red); }
  .person__title { font-size: 12px; font-weight: 700; color: var(--ink); letter-spacing: .5px; margin-top: 2px; }

  .contacts { position: absolute; left: 34px; top: 152px; list-style: none; }
  .contacts li {
    display: flex; align-items: center; gap: 12px;
    font-size: 15px; color: var(--ink);
    margin-bottom: 12px;
  }
  .contacts svg { width: 18px; height: 18px; flex: none; }

  .office {
    position: absolute;
    right: 30px; top: 116px;
    font-size: 13px; line-height: 1.3; color: var(--ink);
    font-style: normal;
  }
  .office__company { font-weight: 700; color: var(--wine); font-size: 14px; }

  .website {
    position: absolute;
    left: 0; right: 0; bottom: 32px;
    text-align: center;
    font-family: "PT Serif", Georgia, serif;
    font-size: 17px;
    letter-spacing: 4px;
    color: var(--on-wine);
  }
</style>
</head>
<body>

<section class="card card--front">
  <svg class="star" viewBox="0 0 24 24" aria-hidden="true">
    <polygon points="12,1 14.9,8.6 23,8.9 16.6,13.9 18.9,21.8 12,17.2 5.1,21.8 7.4,13.9 1,8.9 9.1,8.6" fill="var(--star)"/>
  </svg>
  <div class="company-name">Blue Maple Holdings</div>
  <div class="skyline-band" role="img" aria-label="City skyline silhouette band"></div>
  <p class="tagline">We provides property management services for its residential and commercial properties, in projects throughout California.</p>
</section>

<section class="card card--back">
  <div class="company-name">Blue Maple Holdings</div>
  <div class="rule"></div>

  <div class="person">
    <h1 class="person__name">Dana Whitlock</h1>
    <p class="person__title">FOUNDER &amp; CEO</p>
  </div>

  <ul class="contacts">
    <li>
      <svg viewBox="0 0 20 20" aria-hidden="true"><circle cx="10" cy="10" r="10" fill="var(--wine)"/><path d="M6.5 5.5l2 0 1 2.5-1.3 1a6 6 0 0 0 2.8 2.8l1-1.3 2.5 1v2a1 1 0 0 1-1 1A8.5 8.5 0 0 1 5.5 6.5a1 1 0 0 1 1-1z" fill="#fff"/></svg>
      +1 (555) 014-2290
    </li>
    <li>
      <svg viewBox="0 0 20 20" aria-hidden="true"><circle cx="10" cy="10" r="10" fill="var(--wine)"/><path d="M10 5l5 4.5h-1.5V15h-2.5v-3H9v3H6.5V9.5H5z" fill="#fff"/></svg>
      dw@bluemapleholdings.example
    </li>
  </ul>

  <address class="office">
    <div class="office__company">Blue Maple Holdings Pvt Ltd</div>
    48 Orchard Row, 2nd Floor,<br>Fairview, CT 06000
  </address>

  <div class="skyline-band" role="img" aria-label="City skyline silhouette band"></div>
  <p class="website">www.bluemapleholdings.example</p>
</section>

</body>
</html>
```